Retractable Banner Design for Willowbrook Critters Florida Rebrand

We need a retractable banner design for our market booth. I absolutely love our old banner design and would like to keep it clean and similar but more on theme with the new brand with the new colors. Full brand guide attached. Our slogan we would like to include is "professional pet care for when you can't be there" (dog walking & pet sitting).
Our services we would like to include is: Extended Visits, Pop In Visits, Dog Walking, Pet Taxi, Travel & Adventure Hikes.
We offer: Discounts for First Responders, Teachers, & Military
I would like to use elements from the brand as well as the colors. Include the website www.willowbrookcritters.net somewhere

```html
<!DOCTYPE html>
<html lang="en">
<head>
<meta charset="utf-8">
<title>Willowbrook Critters Florida – Retractable Banner</title>
<link href="https://fonts.googleapis.com/css2?family=Fira+Sans+Extra+Condensed:wght@500;600;700;800&family=Gabriela&family=Open+Sans:wght@700&display=swap" rel="stylesheet">
<style>
  :root {
    --stage: #19191b;
    --paper: #ffffff;
    --teal: #2b5570;
    --magenta: #b83884;
    --ink: #222225;
    --sky: #d5e3ea;
    --sky-soft: #eef4f7;
    --blush: #f6e3ee;
  }
  * { margin: 0; padding: 0; box-sizing: border-box; }
  html, body {
    width: 991px; height: 1200px; overflow: hidden;
    background: var(--stage);
  }
  .banner {
    position: absolute; left: 317px; top: 180px;
    width: 356px; height: 840px;
    background: var(--paper);
    overflow: hidden;
    font-family: "Fira Sans Extra Condensed", sans-serif;
  }
  .brand-name {
    position: absolute; top: 44px; left: 0; width: 100%;
    text-align: center;
    font-family: "Fira Sans Extra Condensed", sans-serif;
    font-weight: 800; color: var(--teal);
    font-size: 40px; line-height: 40px;
  }
  .headline {
    position: absolute; top: 192px; left: 0; width: 100%;
    text-align: center; text-transform: uppercase;
    font-weight: 800; color: var(--teal);
    font-size: 41px; line-height: 35px; letter-spacing: 0.2px;
  }
  .headline .accent { color: var(--magenta); }
  .tagline {
    position: absolute; top: 296px; left: 0; width: 100%;
    text-align: center;
    font-family: "Gabriela", serif;
    color: var(--magenta); font-size: 21px;
  }
  .hero-photo {
    position: absolute; top: 330px; left: 0; width: 356px; height: 260px;
  }
  .services-box {
    position: absolute; left: 35px; top: 595px; width: 286px; height: 131px;
    border: 1.5px solid var(--magenta); border-radius: 12px;
  }
  .section-tab {
    position: absolute; left: 112px; width: 135px; height: 27px;
    background: var(--magenta); color: var(--paper);
    border: 2px solid var(--paper); border-radius: 4px;
    box-shadow: 1px 2px 3px rgba(0,0,0,0.3);
    text-align: center; font-weight: 600;
    font-size: 23px; line-height: 23px;
  }
  .services-tab { top: 582px; }
  .offer-tab { top: 745px; }
  .service {
    position: absolute; width: 110px; margin-left: -55px;
    text-align: center; color: var(--ink);
    font-weight: 500; font-size: 15px; line-height: 16px;
  }
  .service svg { display: block; margin: 0 auto 6px; width: 30px; height: 30px; }
  .offer-text {
    position: absolute; top: 778px; left: 0; width: 100%;
    text-align: center; color: var(--ink);
    font-weight: 500; font-size: 15px;
  }
  .site-band {
    position: absolute; left: 0; bottom: 0; width: 100%; height: 36px;
    background: var(--magenta); color: var(--paper);
    text-align: center; font-family: "Open Sans", sans-serif;
    font-weight: 700; font-size: 15px; line-height: 36px;
  }
</style>
</head>
<body>
<main class="banner">
  <h1 class="brand-name">Willowbrook Critters<br>Florida</h1>

  <h2 class="headline">Professional<br><span class="accent">Pet Care</span> for when<br>you can't be there</h2>
  <p class="tagline">Dog walking &amp; pet sitting.</p>

  <svg class="hero-photo" viewBox="0 0 356 260" role="img" aria-label="Photo of a smiling woman hugging a golden retriever">
    <defs>
      <radialGradient id="heroGlow" cx="0.5" cy="0.35" r="0.75">
        <stop offset="0" stop-color="#ffffff"/>
        <stop offset="0.55" stop-color="#eef4f7"/>
        <stop offset="1" stop-color="#d5e3ea"/>
      </radialGradient>
      <radialGradient id="heroSubject" cx="0.5" cy="0.55" r="0.5">
        <stop offset="0" stop-color="#d9b27c"/>
        <stop offset="0.7" stop-color="#e8d6bd" stop-opacity="0.8"/>
        <stop offset="1" stop-color="#e8d6bd" stop-opacity="0"/>
      </radialGradient>
    </defs>
    <path d="M0 0 H356 V240 Q178 275 0 240 Z" fill="url(#heroGlow)"/>
    <ellipse cx="190" cy="150" rx="150" ry="140" fill="url(#heroSubject)"/>
  </svg>

  <div class="services-box"></div>
  <div class="section-tab services-tab">OUR SERVICES</div>

  <div class="service" style="left:87px; top:614px;">
    <svg viewBox="0 0 30 30"><circle cx="14" cy="16" r="12" fill="none" stroke="#222225" stroke-width="2.5"/><circle cx="14" cy="16" r="8.5" fill="#b83884"/><path d="M14 10v6l4 3" stroke="#fff" stroke-width="1.8" fill="none"/><path d="M24 2a5 5 0 1 0 5 6 4 4 0 1 1-5-6z" fill="#222225"/></svg>
    Extended Visits
  </div>
  <div class="service" style="left:182px; top:614px;">
    <svg viewBox="0 0 30 30"><rect x="13" y="2" width="13" height="26" fill="#222225"/><rect x="16" y="6" width="7" height="2" fill="#fff"/><rect x="16" y="11" width="7" height="2" fill="#fff"/><rect x="16" y="16" width="7" height="2" fill="#fff"/><path d="M7 28c-5-7-6-9-6-12a6 6 0 0 1 12 0c0 3-1 5-6 12z" fill="#b83884"/><circle cx="7" cy="16" r="2.2" fill="#fff"/></svg>
    Pop In Visits
  </div>
  <div class="service" style="left:276px; top:614px;">
    <svg viewBox="0 0 30 30"><circle cx="9" cy="4" r="3" fill="#222225"/><path d="M9 8l-3 8 3 3-2 9M9 8l3 8-1 12M6 12l-3 5M10 11l5 5 6 6" stroke="#222225" stroke-width="2.6" fill="none" stroke-linecap="round"/><path d="M20 24h7l1-3 1 1-1 2v4M20 24v4M27 24v4" stroke="#b83884" stroke-width="2" fill="none" stroke-linecap="round"/></svg>
    Dog Walking
  </div>
  <div class="service" style="left:95px; top:670px;">
    <svg viewBox="0 0 30 30"><path d="M3 25v-6l3-7h14l3 7v6z" fill="#222225"/><rect x="5" y="16" width="16" height="3" fill="#fff"/><rect x="2" y="25" width="5" height="3" fill="#222225"/><rect x="19" y="25" width="5" height="3" fill="#222225"/><circle cx="23" cy="8" r="6.5" fill="#b83884"/><circle cx="23" cy="9.5" r="2" fill="#fff"/><circle cx="20.5" cy="6.5" r="1" fill="#fff"/><circle cx="23" cy="5.5" r="1" fill="#fff"/><circle cx="25.5" cy="6.5" r="1" fill="#fff"/></svg>
    Pet Taxi
  </div>
  <div class="service" style="left:227px; top:670px; width:160px; margin-left:-80px;">
    <svg viewBox="0 0 30 30"><circle cx="14" cy="13" r="11" fill="#222225"/><path d="M9 7c3 0 4 3 7 2s3 4 0 5-2 4-5 3" stroke="#fff" stroke-width="1.5" fill="none"/><path d="M2 25l12-3 3 2-14 3z" fill="#222225"/><path d="M20 28v-8l3-3 2 2 3-2v11z" fill="#b83884"/></svg>
    Travel &amp; Adventure Hikes
  </div>

  <div class="section-tab offer-tab">WE OFFER</div>
  <p class="offer-text">Discounts for First Responders, Teachers, &amp; Military</p>

  <footer class="site-band">www.willowbrookcritters.net</footer>
</main>
</body>
</html>
```